KemaTruvi 16 pages booklet CD Cover

I need a cover (also formatted to be used for digital release), a 16 Pages Booklet + Inlay both sides, a back cover, and a CD image for french pop-rock album.

The name of the artist : Kematruvi
The name of the album : Cueillir la brume (which means "picking the mist")
Style of music: I've attached some mp3 extracts. In a few words, this is electro POP music, I'm inspired by band such as The Quill, etc..

This album talks about the desire to live elsewhere, in a world more just and equitable, less painful. The songs talk about people fighting to find a job, to feed their son, poeple who would like to have enough money to enjoy life, etc... but as they can't, at least, they dream about a new world, they draw this elsewhere, hence the title of the album "Cueillir la brume"

Industry/Entity Type

Music Download

Number of Pages Required

5+ page

Font styles to use
Sans Serif

Colors
b768aa
33a6d7

Requirements
Must have
• COver: fell free to make your porposal as long as it match the project description objectoves.
• I have add/attached a document "CD Cover Structure" that explains the stucture of the cover, and how i think it could be setup. BUt any other proposal will be welcome.
• For the last one, we will put the song titles and i will let you make me some suggestions.
Nice to have
• the songs are rather melancholy (but not sad) and it would be nice to transmit this impression by the colors. That's why i have chose the pink and blue as primary colours.

```html
<!DOCTYPE html>
<html lang="fr">
<head>
<meta charset="utf-8">
<title>Figer le temps — livret</title>
<link rel="stylesheet" href="https://fonts.googleapis.com/css2?family=Amatic+SC:wght@400;700&display=swap">
<style>
  :root {
    --page: #ebdfe8;
    --title: #c0357f;
    --chord: #c0357f;
    --lyric: #2c3550;
    --wash: #dcc7d6;
  }
  * { margin: 0; padding: 0; box-sizing: border-box; }
  html, body { width: 1200px; height: 1200px; overflow: hidden; }
  body { background: var(--page); font-family: "Amatic SC", "Arial Narrow", sans-serif; }
  .booklet-page { position: relative; width: 1200px; height: 1200px; background: var(--page); }
  .wash { position: absolute; }
  .wash--top { top: 0; right: 0; width: 260px; height: 200px;
    background: radial-gradient(ellipse at 70% 30%, var(--wash) 0%, rgba(220,199,214,0) 70%); }
  .wash--bottom { bottom: 0; right: 40px; width: 300px; height: 240px;
    background: radial-gradient(ellipse at 55% 60%, var(--wash) 0%, rgba(220,199,214,0) 70%); }
  .song-title { position: absolute; left: 126px; top: 72px; color: var(--title);
    font-weight: 700; font-size: 112px; line-height: 1; letter-spacing: 1px; }
  .dedication { position: absolute; left: 126px; top: 182px; color: var(--title);
    font-weight: 700; font-size: 40px; line-height: 1; }
  .verse { position: absolute; top: 318px; list-style: none; }
  .verse--left { left: 198px; }
  .verse--right { left: 657px; }
  .line { height: 78px; }
  .chords { position: relative; height: 26px; color: var(--chord); font-weight: 700; font-size: 24px; line-height: 26px; }
  .chords span { position: absolute; top: 0; }
  .lyric { color: var(--lyric); font-weight: 700; font-size: 33px; line-height: 40px; white-space: nowrap; }
</style>
</head>
<body>
<main class="booklet-page">
  <div class="wash wash--top" role="img" aria-label="Tache d'aquarelle rose pâle"></div>
  <div class="wash wash--bottom" role="img" aria-label="Tache d'aquarelle rose pâle"></div>

  <h1 class="song-title">Figer le temps</h1>
  <p class="dedication">(à mon fils qui grandit trop vite)</p>

  <ul class="verse verse--left">
    <li class="line"><div class="chords"><span style="left:0">DE</span><span style="left:120px">F#M</span><span style="left:186px">A</span></div><p class="lyric">A chacun de tes sourires</p></li>
    <li class="line"><div class="chords"><span style="left:0">DE</span><span style="left:178px">F#M</span><span style="left:244px">A</span></div><p class="lyric">A ta main qu'il faut tenir</p></li>
    <li class="line"><div class="chords"><span style="left:180px">D</span><span style="left:333px">E</span></div><p class="lyric">Quand les soucis loin du sol s'envolent</p></li>
    <li class="line"><div class="chords"><span style="left:0">F#M</span></div><p class="lyric">A chaque jour ses parfums,</p></li>
    <li class="line"><div class="chords"><span style="left:0">F#M</span></div><p class="lyric">Ces découvertes sans fin</p></li>
    <li class="line"><div class="chords"><span style="left:120px">D</span></div><p class="lyric">Je garde en moi ces instants</p></li>
    <li class="line"><div class="chords"><span style="left:120px">E</span></div><p class="lyric">Comme un défi au temps</p></li>
    <li class="line"><div class="chords"><span style="left:63px">F#M</span></div><p class="lyric">La candeur comme un drapeau</p></li>
    <li class="line"><div class="chords"><span style="left:63px">F#M</span></div><p class="lyric">La candeur comme un drapeau</p></li>
  </ul>

  <ul class="verse verse--right">
    <li class="line"><div class="chords"><span style="left:0">DE</span><span style="left:178px">F#M</span><span style="left:304px">A</span></div><p class="lyric">Les mots qui viendront trop tôt</p></li>
    <li class="line"><div class="chords"><span style="left:0">DE</span><span style="left:178px">F#M</span><span style="left:238px">A</span></div><p class="lyric">Prendre leur part du gâteau</p></li>
    <li class="line"><div class="chords"><span style="left:46px">D</span></div><p class="lyric">Grignoter l'innocence</p></li>
    <li class="line"><div class="chords"><span style="left:46px">E</span></div><p class="lyric">Préparer ton absence</p></li>
    <li class="line"><div class="chords"><span style="left:0">D</span></div><p class="lyric">Graver les rires et les larmes</p></li>
    <li class="line"><div class="chords"><span style="left:0">E</span></div><p class="lyric">Rester transi sous le charme</p></li>
    <li class="line"><div class="chords"><span style="left:0">F#M</span></div><p class="lyric">Petit nez sous nos mentons</p></li>
    <li class="line"><div class="chords"><span style="left:23px">A</span></div><p class="lyric">Savoir qu'il s'enfuit à tâtons</p></li>
    <li class="line"><div class="chords"><span style="left:63px">D</span></div><p class="lyric">Je voudrais figer le temps</p></li>
  </ul>
</main>
</body>
</html>
```